Dog walking/Pet Sitting company needs a brochure to hook high end apartment tenants

We are looking for a brochure design that we can bring to meetings with high-end apartment and hotel management that will explain who we are, what we do, and how we can help their tenants/guests. I would like it to reflect the same look and feel of our website, carried over to printed brochure. Wesbite is www.hollowbrookpawcare.com. I can provide the stock images from the website if needed. A bi-fold brochure is ideal, unless you feel the information would fit better on a tri-fold. My company colors are #5D4664 and #5BA046. I would like a more professional tone to it, rather than fun.

Target Market(s)

Demo Professional Females and Males ages 30-50 with pets

Industry/Entity Type

Pet sitting

Font styles to use
Sans Serif

Colors
6b449b
9bcb3c

Requirements
Must have
• the same look and feel as my website; explain who we are, what we do, how we can help; include services offered; Mention that we service Parsippany and surrounding towns. Mention 15 years in business.
Should not have
• do not list pricing on brochure (you can mention pricing is available on the website). No cartoonish feel.

```html
<!DOCTYPE html>
<html lang="en">
<head>
<meta charset="utf-8">
<title>Hollowbrook Paw Care – Brochure</title>
<link href="https://fonts.googleapis.com/css2?family=Cabin:wght@500;600;700&family=Source+Sans+3:ital,wght@0,400;0,600;1,400&display=swap" rel="stylesheet">
<style>
:root{
  --stage:#8e8e8e;
  --plum:#5d4664;
  --plum-deep:#4f3a56;
  --green:#5ba046;
  --leaf:#62c43d;
  --ink:#3b3340;
  --paper:#ffffff;
}
*{box-sizing:border-box;margin:0;padding:0}
html,body{width:1200px;height:1200px;overflow:hidden;background:var(--stage)}
body{position:relative;font-family:"Source Sans 3",Arial,sans-serif;color:var(--ink)}
.spread{position:absolute;left:220px;width:762px;height:538px;overflow:hidden;background:var(--paper)}
.spread--outside{top:56px}
.spread--inside{top:630px}
.abs{position:absolute}
.photo{position:absolute}

/* outside: about panel */
.about{left:0;top:0;width:408px;height:538px;background:linear-gradient(160deg,#634b6b,var(--plum-deep));color:#f1ecf3}
.about h2{position:absolute;left:30px;top:30px;font-family:Cabin,sans-serif;font-weight:600;font-size:17px;color:var(--leaf)}
.about .body{position:absolute;left:30px;top:60px;width:302px;font-size:7px;line-height:10px;text-align:justify}
.about .body p{margin-bottom:10px}
.about .sign{font-weight:600;font-size:7.6px;margin-bottom:0 !important}
.about .sign-role{font-style:italic}
.contact{position:absolute;left:128px;top:458px;font-size:7.6px;line-height:13px}
.contact li{list-style:none;display:flex;align-items:center;gap:6px}
.contact svg{width:8px;height:8px}
.contact-rule{position:absolute;left:124px;top:506px;width:208px;height:1px;background:rgba(255,255,255,.35)}
.seal{position:absolute;left:304px;top:448px;width:56px;height:56px;border:1.5px solid #fff;border-radius:50%}

/* outside: cover */
.cover{left:408px;top:0;width:354px;height:538px;background:linear-gradient(180deg,#fbf8f4 0%,#f1e6d8 40%,#c9b39c 100%)}
.brand{position:absolute;right:16px;top:58px;width:190px;text-align:center}
.brand-dot{width:30px;height:30px;border-radius:50%;background:var(--plum);margin:0 auto 10px}
.brand-name{font-family:Cabin,sans-serif;font-weight:600;font-size:12.5px;letter-spacing:.2px;color:var(--plum);white-space:nowrap}
.cover-band{position:absolute;left:86px;top:424px;width:268px;height:102px;background:var(--plum);color:#fff;text-align:right;padding:10px 14px 0 0;font-family:Cabin,sans-serif}
.cover-band .lead{font-weight:600;font-size:14px;line-height:19.5px}
.cover-band .focus{font-weight:600;font-size:14px;color:var(--leaf);margin-top:8px}
.cover-band .url{font-family:"Source Sans 3",sans-serif;font-size:9.5px;letter-spacing:.6px;margin-top:9px}

/* inside */
.fold{position:absolute;left:381px;top:0;width:12px;height:538px;background:linear-gradient(90deg,rgba(0,0,0,.08),rgba(0,0,0,0))}
.services-bar{position:absolute;left:0;top:24px;width:334px;height:27px;background:var(--plum);border-radius:0 6px 6px 0;color:#fff;font-family:Cabin,sans-serif;font-weight:500;font-size:15.5px;line-height:27px;padding-left:30px}
.svc{position:absolute;font-size:6.4px;line-height:8.4px}
.svc h3{font-family:Cabin,sans-serif;font-weight:600;font-size:10.5px;color:var(--plum);margin-bottom:5px}
.svc .note{font-style:italic;margin-bottom:3px}
.svc ul{list-style:none}
.svc li{position:relative;padding-left:9px;margin-bottom:4.3px}
.svc li::before{content:"";position:absolute;left:0;top:2px;width:3.5px;height:3.5px;border:1px solid var(--green);border-radius:50%}
.svc p{text-align:justify;margin-bottom:6px}
.svc-tail{position:absolute;left:411px;width:320px;font-size:6.4px;line-height:8.4px;text-align:justify}
</style>
</head>
<body>

<section class="spread spread--outside">
  <div class="abs about">
    <h2>About Us</h2>
    <div class="body">
      <p>We specialize in one-to-one personalized, quality pet care. We offer many services to cater to your needs. Whether you have dogs, cats, reptiles or rodents, we can help!</p>
      <p>Our business was born out of necessity. There were very few options for pet owners as recently as 15 years ago for pet care when pet owners needed to travel or work long hours. We were in the same boat, with a new puppy and both “mom and dad” working in an industry that took us away from our fur-baby for ten hours a day and business trips that didn’t allow an extra carry-on with fur sticking out! How would we ever find someone we trusted enough to care for our baby boy? Other pet owners must be resonating with these same feelings of guilt, worry and fear.</p>
      <p>I imagined a company that could provide peace of mind for pet owners. I knew that my vision would allow others to enjoy the benefits of pet ownership, while maintaining their careers, social lives and family time without holding on to the guilt. I gave up my corporate career because of this belief. I wish I could say it was the hardest thing I have ever done, but in fact it was blissfully easy, because it was meant to be. I found my path and with a lot of hard work and long hours, my vision became a reality.</p>
      <p>Today, we are a fully-staffed company with employees (not independent contractors) who are as excited about working with pets as I am. We are continually educating ourselves and when we are not caring for pets, we are studying coursework on how to be better in-tune with dog behavior, pet health and related topics (we are a PawSkill Certified business). We truly pride ourselves on giving the pets we care for a full “experience” and not just a walk. The love I have seen from my staff warms my heart and gives me hope for this world!</p>
      <p>If you have pets and experience any feelings of guilt when you need to leave them behind, reach out to us! We pick right up where you leave off, with smiles, love and adventures that can turn an ordinary day extraordinary!</p>
      <p class="sign">Dana Whitcombe,</p>
      <p class="sign-role">Owner, Hollowbrook Paw Care LLC</p>
    </div>
    <div class="photo" role="img" aria-label="Small terrier dog holding a leather leash in its mouth" style="left:12px;top:400px;width:112px;height:120px;background:radial-gradient(ellipse at 50% 55%,#c89a6e 0%,#a77a55 45%,rgba(93,70,100,0) 72%)"></div>
    <ul class="contact">
      <li><svg viewBox="0 0 10 10"><path d="M2 1l2 2-1 1.3c.6 1.2 1.5 2.1 2.7 2.7L7 6l2 2-1.2 1.2C4.5 9 1 5.5.8 2.2z" fill="var(--leaf)"/></svg>201-555-0148</li>
      <li><svg viewBox="0 0 10 10"><rect x=".5" y="2" width="9" height="6.5" fill="none" stroke="var(--leaf)"/><path d="M.5 2l4.5 3.5L9.5 2" fill="none" stroke="var(--leaf)"/></svg>hello@hollowbrookpawcare.com</li>
      <li><svg viewBox="0 0 10 10"><circle cx="5" cy="5" r="4.3" fill="none" stroke="var(--leaf)"/><path d="M.7 5h8.6M5 .7c-2.4 2.6-2.4 6 0 8.6M5 .7c2.4 2.6 2.4 6 0 8.6" fill="none" stroke="var(--leaf)" stroke-width=".8"/></svg>www.hollowbrookpawcare.com</li>
    </ul>
    <div class="contact-rule"></div>
    <div class="seal"></div>
  </div>

  <div class="abs cover">
    <div class="photo" role="img" aria-label="Smiling woman on a sofa hugging a black and white spaniel" style="left:0;top:120px;width:354px;height:418px;background:radial-gradient(ellipse at 55% 45%,#e9c9a2 0%,#8c7a6c 40%,rgba(201,179,156,0) 75%)"></div>
    <div class="brand">
      <div class="brand-dot"></div>
      <div class="brand-name">HOLLOWBROOK PAW CARE</div>
    </div>
    <div class="cover-band">
      <div class="lead">Prioritize Your Family, Career,<br>Health, Social Life ,Goals,Yourself.</div>
      <div class="focus">We'll Focus on Your Pets.</div>
      <div class="url">www.hollowbrookpawcare.com</div>
    </div>
  </div>
</section>

<section class="spread spread--inside">
  <div class="fold"></div>
  <div class="services-bar">PROFESSIONAL PET CARE SERVICES</div>

  <div class="svc" style="left:30px;top:57px;width:330px">
    <h3>Dog Walking</h3>
    <div class="note">We are pleased to provide dog walking services Monday-Friday between the hours of 10:00 am and 5:00 pm.</div>
    <ul style="width:198px">
      <li>Walking your dog (we offer a standard untimed visit and a guaranteed one-hour visit)</li>
      <li>Providing healthy exercise and fun</li>
      <li>Cleaning your dog after coming in from outside</li>
      <li>Feeding your dog and/or providing fresh water/treats</li>
      <li>Training reinforcement</li>
      <li>Grooming &amp; pampering your dog, such as brushing out coat</li>
      <li>Light pet-related housekeeping (cleaning up accidents or food/water spills)</li>
      <li>Bringing in your mail/packages</li>
      <li>Providing you with an emailed/texted report along with photos</li>
    </ul>
  </div>
  <div class="photo" role="img" aria-label="Yellow labrador carrying a blue leash" style="left:234px;top:97px;width:116px;height:110px;background:linear-gradient(135deg,#c98a2e,#f0d8a6 60%,#e9e4d8)"></div>

  <div class="svc" style="left:30px;top:218px;width:320px">
    <h3>Pet Sitting</h3>
    <div class="note">We are pleased to provide pet sitting services 7 days a week during the following times: 7:30 am – 9:30 am; 12:00 pm – 4:00 pm; 7:30 pm – 9:30 pm</div>
    <ul>
      <li>Three untimed visits throughout the day (morning, afternoon, evening) to ensure a happy &amp; comfortable pet (we offer a standard untimed visit and a guaranteed one-hour visit)</li>
    </ul>
    <ul style="width:190px">
      <li>Inclusive of all pets within the household</li>
      <li>Walking your dog and playing with your cat or other household pets</li>
      <li>Providing healthy, fun exercise</li>
      <li>Cleaning your dog after coming in from outside</li>
      <li>Feeding your dog &amp; providing fresh water/treats</li>
      <li>Emailed visit reports and pictures of your pets</li>
      <li>Pet sitting visits also include home care at no additional cost. This may include bringing in mail/packages, taking out the trash, sweeping the floors, watering plants, etc.</li>
    </ul>
  </div>
  <div class="photo" role="img" aria-label="Dog eating from a metal food bowl" style="left:234px;top:277px;width:116px;height:111px;background:linear-gradient(160deg,#f4ece0,#d9b27a 55%,#8a6a48)"></div>

  <div class="svc" style="left:30px;top:400px;width:192px">
    <h3>Sleepovers</h3>
    <p>Our newest option is becoming increasingly popular with pet parents who want to leave their pets home, but not alone, overnight. Now we can arrange to have a sitter stay with your pets overnight in the comfort of your home (from 10 pm to 7 am). This option includes a late-night walk and an early morning walk. Mid-day visits are additional and can be supplemented as needed. This service includes any home care services you may need while you are away at no additional charge. It includes care for all pets in your household.</p>
  </div>
  <div class="photo" role="img" aria-label="Woman resting her head beside a sleeping brown dog" style="left:233px;top:404px;width:116px;height:112px;background:linear-gradient(150deg,#efe9e4,#a9897a 55%,#5b4238)"></div>

  <div class="svc" style="left:411px;top:26px;width:195px">
    <h3>Cat Sitting/Small Pet Sitting</h3>
    <ul>
      <li>One untimed visit per day (we stay until your cat is content!)</li>
      <li>Socializing and playing with your cat</li>
      <li>Providing healthy mental stimulation and play</li>
      <li>Scooping litter box daily and full cleaning as needed</li>
      <li>Feeding your cat, providing fresh water/treats and cleaning the feeding area</li>
      <li>Emailed visit reports and pictures of your pet</li>
      <li>Cat sitting visits also may include basic home care at no additional cost. This may include bringing in the mail and packages, taking out the trash, sweeping the floors, watering plants, etc.</li>
    </ul>
  </div>
  <div class="photo" role="img" aria-label="Grey tabby cat being petted" style="left:615px;top:29px;width:117px;height:111px;background:linear-gradient(140deg,#dfe3ea,#a9a6a3 55%,#6f7587)"></div>

  <div class="svc" style="left:411px;top:180px;width:192px">
    <h3>Day Care &amp; Overnight Boarding</h3>
    <p>We understand that leaving your dog at home or in a kennel is not always the best option. That’s why we offer leaving your dog(s) with us at our home. We accept smaller breed dogs (approximately 30lbs or less) who are fully house-broken, neutered/spayed, and socialize well with other dogs. All vaccinations must be current, including rabies, DHLP/Parvo, and Bordetella.</p>
    <p style="margin-bottom:0">While staying in our home, your dog will enjoy walks by the lake, playtime in our fenced-in yard, and sleeping and playing inside our doggie playroom. We try to limit the number of guests in order to maintain a relatively peaceful and calm atmosphere. We do not crate your dog unless you specify</p>
  </div>
  <div class="photo" role="img" aria-label="Three dogs peeking out from under a striped blanket" style="left:614px;top:200px;width:117px;height:112px;background:linear-gradient(180deg,#8a6a5a,#5b4a48 50%,#b08b86)"></div>
  <p class="svc-tail" style="top:318px">we do. We provide dog beds, bowls and toys; you provide their food and whatever else will make their stay more comfortable!</p>

  <div class="svc" style="left:411px;top:362px;width:192px">
    <h3>Wedding Attendant</h3>
    <p style="margin-bottom:0">When they are a part of your family, they should also be a part of your wedding! We can help make your wedding dreams a reality–or at least make sure your wedding dress stays white and your tux stays black! Our deluxe wedding service includes everything you need to prep your pooch for the big event (maybe they need a bath, trip to and from the groomer, or just help to get dressed for the celebration), transporting them to and from the service, chaperoning them during your photo session, walking them down the aisle, sitting with them during the ceremony, having them politely greet guests, and joining the party at cocktail hour and/or your reception. Every step of the way, we are focused on making sure that your pet is calm and happy so you can enjoy the best day of your lives! Each part of</p>
  </div>
  <div class="photo" role="img" aria-label="White dog sitting on grass with a couple behind" style="left:615px;top:368px;width:117px;height:111px;background:linear-gradient(160deg,#6d8a6a,#a9b79a 50%,#eae6dc)"></div>
  <p class="svc-tail" style="top:500px">this service can be customized to fit your needs. A wedding pet care coordinator will meet with you prior to the event to hand-craft an itinerary so no detail is overlooked. Check out our blog to get a behind-the-scenes look at a recent wedding we attended!</p>
</section>

</body>
</html>
```